Company is Valcrest Plumbing.
name Darwin Ashcombe, I am a plumber, drainer, gasfitter and roofer
Mobile: 0471 936 504
Email address: info@valcrestplumbing.example (check out my website for some ideas)
Website: www.valcrestplumbing.example
ABN: 82 193 604 718
LIC: 514906K

I am reliable all round plumber. I am a 24 hour emergency service. Valcrest Plumbing is a professional plumbing service in the Illawarra, South Coast, Southern Sydney and Southern Highland regions of NSW. We offer a 24 hour emergency service for piece of mind to our customers. Call us now to see how we can help you. Valcrest Plumbing approaches every job with attention to detail and excellent customer service. With our superior workmanship you can be confident that the job will be done right the first time around. You can rest assured with results that are guaranteed to last.

Target Market(s)

the general public

Contact Information for Business Card

look up website for some ideas something with similar colours to logo and new modern and to catch the eye.

Colors
fdfdfd
ffffff
000000
7f7f7f
aaaaaa
33a6d7
0492cd

Requirements
Must have
• all contact details
• company- Valcrest Plumbing
• name- Darwin Ashcombe
• number mobile- 0471 936 504
• Email address- info@valcrestplumbing.example
• Website- www.valcrestplumbing.example
• ABN- 82 193 604 718
• LIC- 514906K

```html
<!DOCTYPE html>
<html lang="en">
<head>
<meta charset="utf-8">
<title>Valcrest Plumbing – Business Card</title>
<link rel="stylesheet" href="https://fonts.googleapis.com/css2?family=Roboto:wght@400;500&display=swap">
<style>
  :root {
    --page-bg: #d9d6d2;
    --card-top: #1c1c1e;
    --card-bottom: #050505;
    --brand-blue: #0492cd;
    --name-blue: #1f6f93;
    --text-light: #e6e6e6;
    --text-grey: #aaaaaa;
    --text-warm: #c9bda8;
    --pipe-grey: #7f7f7f;
  }
  * { margin: 0; padding: 0; box-sizing: border-box; }
  html, body {
    width: 1200px; height: 969px; overflow: hidden;
    background: var(--page-bg);
    font-family: "Roboto", Arial, sans-serif;
  }
  .card {
    position: absolute; left: 150px; top: 225px;
    width: 928px; height: 527px;
    background: linear-gradient(160deg, var(--card-top) 0%, var(--card-bottom) 55%, #111 100%);
    box-shadow: 0 10px 30px rgba(0,0,0,.35);
    overflow: hidden;
  }
  .emblem {
    position: absolute; left: 58px; top: 63px;
    width: 260px; height: 260px;
    display: flex; flex-direction: column; align-items: center; justify-content: center;
    gap: 6px;
  }
  .emblem-dot {
    width: 26px; height: 26px; border-radius: 50%;
    background: var(--brand-blue);
    margin-bottom: 10px;
  }
  .emblem-name {
    color: var(--brand-blue);
    font-weight: 500; font-size: 32px; letter-spacing: 3px;
    text-transform: uppercase; line-height: 1.1; text-align: center;
  }
  .wordmark {
    position: absolute; right: 53px; top: 108px;
    color: var(--brand-blue);
    font-weight: 500; font-size: 40px; letter-spacing: 4px;
    text-transform: uppercase; text-align: right; line-height: 1.2;
  }
  .contact {
    position: absolute; right: 53px; top: 232px;
    text-align: right; font-size: 21px; line-height: 31px;
    color: var(--text-light);
  }
  .contact .email { color: var(--text-warm); }
  .contact .ids { margin-top: 12px; color: var(--text-grey); line-height: 29px; }
  .pipe {
    position: absolute; left: 220px; top: 392px;
    width: 708px; height: 9px;
  }
  .holder-name {
    position: absolute; left: 80px; top: 458px;
    color: var(--name-blue);
    font-size: 29px; font-weight: 400; text-transform: uppercase;
    letter-spacing: .5px;
  }
  .website {
    position: absolute; right: 53px; top: 462px;
    font-size: 21px; color: var(--text-warm);
  }
  .website .domain { color: var(--name-blue); }
</style>
</head>
<body>
  <div class="card">
    <div class="emblem">
      <span class="emblem-dot"></span>
      <span class="emblem-name">Valcrest<br>Plumbing</span>
    </div>

    <div class="wordmark">Valcrest<br>Plumbing</div>

    <div class="contact">
      <p class="phone">0471 936 504</p>
      <p class="email">info@valcrestplumbing.example</p>
      <div class="ids">
        <p>ABN- 82 193 604 718</p>
        <p>LIC- 514906K</p>
      </div>
    </div>

    <svg class="pipe" viewBox="0 0 708 9" preserveAspectRatio="none" aria-hidden="true">
      <defs>
        <linearGradient id="pipe-shade" x1="0" y1="0" x2="0" y2="1">
          <stop offset="0" stop-color="#9a9a9a"/>
          <stop offset="1" stop-color="#4a4a4a"/>
        </linearGradient>
      </defs>
      <rect x="0" y="0" width="708" height="9" fill="url(#pipe-shade)"/>
    </svg>

    <p class="holder-name">Darwin Ashcombe</p>
    <p class="website">www.<span class="domain">valcrestplumbing</span>.example</p>
  </div>
</body>
</html>
```